make it look old timey and motherly but mordern...bath soak with cooling vapors. tall pine hush

need a bath soak label...cooling vapors. will be in a pouch like below. dont pay attention to the design, just attatching so you know the kind of pouch itll be in. need something trusty, minimal and clean...its called tall pine hush bath soak the best bath yull ever take.... for sore muscles, cooling vapors, smells good...made with menthol lemon and eucalyptus...give me something good.

Target Market(s)

make it look old timey and motherly but mordern

Font styles to use
Serif
Sans Serif

Colors
0054AA
0677BA
7BADD7
CADEEF
E8F1F8
0094D4
00A9DD
6FCCEA
C7EBF8
E9F6FB
FFF300
FFF600
FEFA6F
FFFEC7
FFFEE8
FFC000
F8CF3A
FAE287
FDF2CF
FEFAEE
E54698
E96AAD
F1A4CE
F9D9EA
FCEFF6
6B429C
8869AF
B7A5CE
E3DAEB
F3F0F8

```html
<!DOCTYPE html>
<html lang="en">
<head>
<meta charset="utf-8">
<title>tall pine hush — Bath Soak</title>
<link href="https://fonts.googleapis.com/css2?family=Fraunces:opsz,wght@9..144,600;9..144,800&display=swap" rel="stylesheet">
<style>
  :root {
    --backdrop: #ececec;
    --pink-light: #f06aa8;
    --pink-core: #fb0a7f;
    --pink-deep: #b8005c;
    --ornament-tint: #f7b9d6;
    --ink-white: #ffffff;
  }
  html, body {
    margin: 0;
    padding: 0;
    width: 1190px;
    height: 1200px;
    overflow: hidden;
    background: var(--backdrop);
  }
  .canvas {
    position: relative;
    width: 1190px;
    height: 1200px;
    display: flex;
    align-items: center;
    justify-content: center;
  }
  .label {
    position: relative;
    width: 480px;
    height: 760px;
    border-radius: 10px;
    overflow: hidden;
    background:
      radial-gradient(ellipse 70% 55% at 50% 62%, var(--pink-core) 0%, rgba(251,10,127,0) 70%),
      linear-gradient(180deg, var(--pink-light) 0%, #f53c93 40%, var(--pink-core) 68%, var(--pink-deep) 100%);
    color: var(--ink-white);
    font-family: "Fraunces", Georgia, serif;
  }
  .floral-ornament {
    position: absolute;
    left: 0;
    top: 0;
    width: 360px;
    height: 310px;
    border-bottom-right-radius: 70% 80%;
    background: radial-gradient(ellipse at 28% 35%, rgba(247,185,214,0.75) 0%, rgba(247,185,214,0.35) 55%, rgba(247,185,214,0) 100%);
  }
  .brand-name {
    position: absolute;
    left: 42px;
    top: 485px;
    margin: 0;
    font-weight: 800;
    font-size: 62px;
    line-height: 0.9;
    letter-spacing: -0.02em;
  }
  .product-type {
    position: absolute;
    left: 46px;
    top: 685px;
    margin: 0;
    font-weight: 600;
    font-size: 19px;
    letter-spacing: 0.22em;
    text-transform: uppercase;
  }
  .scent-block {
    position: absolute;
    right: 38px;
    top: 548px;
    text-align: right;
  }
  .scent-notes {
    margin: 0;
    font-weight: 800;
    font-size: 26px;
    line-height: 1.05;
    letter-spacing: -0.01em;
  }
  .benefits {
    margin: 12px 0 0;
    font-weight: 600;
    font-size: 17px;
    line-height: 1.1;
  }
</style>
</head>
<body>
  <main class="canvas">
    <section class="label">
      <div class="floral-ornament" role="img" aria-label="Line-art floral mandala ornament in light pink"></div>
      <h1 class="brand-name">tall<br>pine<br>hush</h1>
      <p class="product-type">Bath Soak</p>
      <div class="scent-block">
        <p class="scent-notes">menthol,<br>lemon &amp;<br>eucalyptus</p>
        <p class="benefits">for sore muscles<br>cooling vapors</p>
      </div>
    </section>
  </main>
</body>
</html>
```